Social media app sign-up flow that asks users to give personal info and connect with other apps

Design an interactive, fun, and playful sign-up flow in which you are providing information about you, your interests, and connecting with different API plug-ins such as Plazabell, Workvane, Tunequill, etc. (using the brand palette attached).

Basic wireframe, and business requirements are also attached.

Target Market(s)

Gen Z + Millennials (ages 22-40)

Font styles to use
Sans Serif

Colors
fbed22
fbee3d
fbf289

Requirements
Must have
• Forms for users to submit their info. Follow the color palette attached.

Connect with Plazabell, Connect with Workvane, Connect with Tunequill, Connect with Gatherloop buttons
Nice to have
• I like the way you can use cards to submit your information for each category. Interactive card design for providing your info
Should not have
• Basic outdated designs, long forms

```html
<!DOCTYPE html>
<html lang="en">
<head>
<meta charset="utf-8">
<title>Sign-up Flow</title>
<link href="https://fonts.googleapis.com/css2?family=Montserrat:wght@400;500;600;800;900&display=swap" rel="stylesheet">
<style>
  :root{
    --stage:#141414;
    --yellow:#fbc230;
    --yellow-soft:#fde7a6;
    --white:#ffffff;
    --card:#f6f6f7;
    --ink:#1c1c1c;
    --muted:#8a8a8a;
    --line:#d9d9d9;
    --mail:#dc4a3d;
    --plaza:#4a67ad;
    --orchard:#111111;
    --work:#0e76a8;
    --tune:#1fcf5e;
  }
  *{box-sizing:border-box;margin:0;padding:0}
  html,body{width:1200px;height:932px;overflow:hidden;background:var(--stage);font-family:"Montserrat",sans-serif;color:var(--ink)}
  .flow{display:flex;gap:24px;padding:166px 24px 0;width:1200px;height:932px}
  .screen{width:270px;height:600px;background:var(--white);border-radius:6px;overflow:hidden;position:relative;box-shadow:0 20px 40px rgba(0,0,0,.5)}
  .header{background:var(--yellow);height:170px;border-bottom-right-radius:90px;padding:46px 22px 0;color:var(--white);position:relative}
  .body{background:var(--white);margin-top:-56px;border-top-left-radius:56px;position:relative;padding:26px 20px 0}
  .back{position:absolute;left:14px;top:16px;width:16px;height:16px}
  .kicker{font-size:15px;font-weight:400;line-height:1.1}
  .title{font-size:24px;font-weight:900;line-height:1.05;letter-spacing:.5px}
  .title-sm{font-size:17px;font-weight:800;line-height:1.15}
  .sub{font-size:17px;font-weight:400;line-height:1}
  .lead{font-size:13px;font-weight:800}
  .note{font-size:9.5px;color:#444;line-height:1.35}
  .center{text-align:center}
  .phone-row{display:flex;gap:8px;margin:14px 0 10px}
  .country{width:52px;height:30px;border:1px solid var(--line);border-radius:3px;display:flex;align-items:center;justify-content:center;gap:4px;font-size:9px}
  .country .flag{width:16px;height:11px;background:#2a3f8f;border-radius:1px}
  .field{flex:1;height:30px;background:var(--card);border:1px solid #ececec;border-radius:3px;font-size:10px;color:#aaa;display:flex;align-items:center;padding:0 10px;justify-content:space-between}
  .btn{height:32px;border-radius:3px;display:flex;align-items:center;color:var(--white);font-size:10px;font-weight:600;margin-bottom:8px;overflow:hidden}
  .btn .mark{width:32px;height:32px;background:rgba(0,0,0,.18);flex:none}
  .btn .label{flex:1;text-align:center}
  .btn-primary{background:var(--yellow);justify-content:center}
  .btn-mail{background:var(--mail)}
  .btn-plaza{background:var(--plaza)}
  .btn-orchard{background:var(--orchard)}
  .btn-work{background:var(--work)}
  .btn-tune{background:var(--tune)}
  .divider{display:flex;align-items:center;gap:10px;font-size:9px;color:var(--muted);margin:12px 0}
  .divider::before,.divider::after{content:"";flex:1;height:1px;background:var(--line)}
  .legal{font-size:8.5px;color:#555;text-align:center;line-height:1.5;margin-top:12px}
  .legal a,.accent{color:var(--yellow);text-decoration:none;font-weight:600}
  .category-grid{display:grid;grid-template-columns:1fr 1fr;gap:12px 14px;margin-top:18px}
  .category{height:76px;background:var(--card);border-radius:14px;display:flex;flex-direction:column;align-items:center;justify-content:center;gap:6px}
  .category svg{width:32px;height:32px}
  .category span{font-size:9px;font-weight:800;letter-spacing:1.5px;color:var(--yellow);text-transform:uppercase}
  .people-grid{display:grid;grid-template-columns:repeat(3,1fr);gap:10px;margin-top:16px}
  .portrait{height:66px;border-radius:12px}
  .music-row{display:flex;gap:10px;align-items:center;margin-bottom:10px}
  .avatar{width:44px;height:44px;border-radius:4px;flex:none}
  .add-more{font-size:10px;margin:2px 0 0 54px}
  .pencil{width:10px;height:10px}
</style>
</head>
<body>
<main class="flow">

  <!-- Sign up -->
  <section class="screen">
    <header class="header">
      <p class="title-sm">Enjoy events nearby<br>and meet new<br>friends</p>
    </header>
    <div class="body">
      <p class="lead">What's your number?</p>
      <p class="note">We'll text code to verify this number</p>
      <div class="phone-row">
        <div class="country"><span class="flag"></span>▾</div>
        <div class="field">01-2345-678-0</div>
      </div>
      <div class="btn btn-primary">Continue</div>
      <div class="divider">or</div>
      <div class="btn btn-mail"><span class="mark"></span><span class="label">Continue with E-mail</span></div>
      <div class="btn btn-plaza"><span class="mark"></span><span class="label">Continue with Plazabell</span></div>
      <div class="btn btn-orchard"><span class="mark"></span><span class="label">Continue with Orchardly</span></div>
      <div class="btn btn-work"><span class="mark"></span><span class="label">Continue with Workvane</span></div>
      <p class="legal">By signing up you accept the <a href="#">Terms of Service</a> and <a href="#">Privacy Policy</a></p>
      <p class="legal">Already have an account? <a href="#">Log in</a></p>
    </div>
  </section>

  <!-- About you -->
  <section class="screen">
    <header class="header">
      <p class="kicker">Tell me</p>
      <p class="title">ABOUT YOU</p>
    </header>
    <div class="body">
      <p class="note center">You can start where you are and change<br>everything you want</p>
      <div class="category-grid">
        <div class="category">
          <svg viewBox="0 0 32 32"><path d="M4 16 16 5l12 11v12H4z" fill="var(--yellow)" stroke="var(--ink)" stroke-width="2" stroke-linejoin="round"/><rect x="12" y="19" width="8" height="9" fill="var(--white)" stroke="var(--ink)" stroke-width="2"/></svg>
          <span>Places</span>
        </div>
        <div class="category">
          <svg viewBox="0 0 32 32"><path d="M2 12 16 5l14 7-14 7z" fill="var(--yellow)" stroke="var(--ink)" stroke-width="2" stroke-linejoin="round"/><path d="M8 15v7c4 4 12 4 16 0v-7" fill="none" stroke="var(--ink)" stroke-width="2"/></svg>
          <span>Schools</span>
        </div>
        <div class="category">
          <svg viewBox="0 0 32 32"><rect x="4" y="10" width="24" height="17" rx="2" fill="var(--yellow)" stroke="var(--ink)" stroke-width="2"/><path d="M12 10V6h8v4" fill="none" stroke="var(--ink)" stroke-width="2"/></svg>
          <span>Work</span>
        </div>
        <div class="category">
          <svg viewBox="0 0 32 32"><circle cx="16" cy="11" r="6" fill="var(--yellow)" stroke="var(--ink)" stroke-width="2"/><path d="M5 28c1-7 6-9 11-9s10 2 11 9z" fill="var(--yellow)" stroke="var(--ink)" stroke-width="2"/></svg>
          <span>People</span>
        </div>
        <div class="category">
          <svg viewBox="0 0 32 32"><rect x="4" y="7" width="24" height="21" rx="2" fill="var(--yellow)" stroke="var(--ink)" stroke-width="2"/><path d="M4 13h24M10 4v6M22 4v6" stroke="var(--ink)" stroke-width="2"/><path d="m11 20 4 4 7-7" fill="none" stroke="var(--ink)" stroke-width="2"/></svg>
          <span>Events</span>
        </div>
        <div class="category">
          <svg viewBox="0 0 32 32"><rect x="4" y="7" width="24" height="21" rx="2" fill="var(--yellow)" stroke="var(--ink)" stroke-width="2"/><path d="M4 13h24M10 4v6M22 4v6M9 18h14M9 23h10" stroke="var(--ink)" stroke-width="2"/></svg>
          <span>Events</span>
        </div>
        <div class="category">
          <svg viewBox="0 0 32 32"><path d="M12 23V7l14-3v16" fill="none" stroke="var(--ink)" stroke-width="2"/><circle cx="8" cy="24" r="4" fill="var(--yellow)" stroke="var(--ink)" stroke-width="2"/><circle cx="22" cy="21" r="4" fill="var(--yellow)" stroke="var(--ink)" stroke-width="2"/></svg>
          <span>Music</span>
        </div>
        <div class="category">
          <svg viewBox="0 0 32 32"><circle cx="16" cy="9" r="4" fill="var(--yellow)" stroke="var(--ink)" stroke-width="2"/><circle cx="7" cy="15" r="3" fill="var(--yellow)" stroke="var(--ink)" stroke-width="2"/><circle cx="25" cy="15" r="3" fill="var(--yellow)" stroke="var(--ink)" stroke-width="2"/><path d="M9 28c0-8 14-8 14 0z" fill="var(--yellow)" stroke="var(--ink)" stroke-width="2"/></svg>
          <span>Team</span>
        </div>
      </div>
    </div>
  </section>

  <!-- People -->
  <section class="screen">
    <header class="header">
      <svg class="back" viewBox="0 0 16 16"><path d="M10 3 5 8l5 5" fill="none" stroke="var(--white)" stroke-width="1.6"/></svg>
      <p class="title">PEOPLE</p>
      <p class="sub">You know</p>
    </header>
    <div class="body">
      <p class="note center">Fill out automatically with your social<br>media profile</p>
      <div class="btn btn-plaza" style="margin-top:12px"><span class="mark"></span><span class="label">Sync with Plazabell</span></div>
      <div class="divider" style="margin:10px 0 0"></div>
      <div class="people-grid">
        <div class="portrait" role="img" aria-label="Profile photo of a friend" style="background:linear-gradient(135deg,#3a2a22,#a07050)"></div>
        <div class="portrait" role="img" aria-label="Profile photo of a friend" style="background:linear-gradient(135deg,#2e3b45,#8fa1ad)"></div>
        <div class="portrait" role="img" aria-label="Profile photo of a friend" style="background:linear-gradient(135deg,#4a6a70,#c9d6d6)"></div>
        <div class="portrait" role="img" aria-label="Profile photo of a friend" style="background:linear-gradient(135deg,#1c1c1c,#6b3a34)"></div>
        <div class="portrait" role="img" aria-label="Profile photo of a friend" style="background:linear-gradient(135deg,#e8eee8,#d9b99c)"></div>
        <div class="portrait" role="img" aria-label="Profile photo of a friend" style="background:linear-gradient(135deg,#e07a2e,#6a4230)"></div>
        <div class="portrait" role="img" aria-label="Profile photo of a friend" style="background:linear-gradient(135deg,#dde3ea,#2d4a6a)"></div>
        <div class="portrait" role="img" aria-label="Profile photo of a friend" style="background:linear-gradient(135deg,#f1f4f2,#2fc6a2)"></div>
        <div class="portrait" role="img" aria-label="Profile photo of a friend" style="background:linear-gradient(135deg,#5a1620,#b05040)"></div>
        <div class="portrait" role="img" aria-label="Profile photo of a friend" style="background:linear-gradient(135deg,#c9a486,#7a5a48)"></div>
        <div class="portrait" role="img" aria-label="Profile photo of a friend" style="background:linear-gradient(135deg,#6d7a50,#d8a46a)"></div>
        <div class="portrait" role="img" aria-label="Profile photo of a friend" style="background:linear-gradient(135deg,#1a1f1c,#4c5a50)"></div>
      </div>
    </div>
  </section>

  <!-- Music -->
  <section class="screen">
    <header class="header">
      <svg class="back" viewBox="0 0 16 16"><path d="M10 3 5 8l5 5" fill="none" stroke="var(--white)" stroke-width="1.6"/></svg>
      <p class="title">MUSIC</p>
      <p class="sub">You love</p>
    </header>
    <div class="body">
      <p class="note" style="margin:0 0 10px 54px">Fill out manually</p>
      <div class="music-row">
        <div class="avatar" role="img" aria-label="Artist photo" style="background:linear-gradient(135deg,#d8d8d8,#5a5a5a)"></div>
        <div class="field" style="height:36px;color:#555">Mara Delle <svg class="pencil" viewBox="0 0 10 10"><path d="M1 9l1-3 5-5 2 2-5 5z" fill="var(--yellow)"/></svg></div>
      </div>
      <div class="music-row">
        <div class="avatar" role="img" aria-label="Band photo" style="background:linear-gradient(135deg,#2a2a2a,#9a9a9a)"></div>
        <div class="field" style="height:36px;color:#555">The Lanterns <svg class="pencil" viewBox="0 0 10 10"><path d="M1 9l1-3 5-5 2 2-5 5z" fill="var(--yellow)"/></svg></div>
      </div>
      <p class="add-more accent">+ Add More Here</p>
      <div class="divider">or</div>
      <p class="note center">Fill out automatically with your social<br>media profile</p>
      <div class="btn btn-plaza" style="margin-top:12px"><span class="mark"></span><span class="label">Connect with Plazabell</span></div>
      <div class="btn btn-tune"><span class="mark"></span><span class="label">Connect with Tunequill</span></div>
    </div>
  </section>

</main>
</body>
</html>
```